Refinement of Website & Relaymark Integration

We are launching a new business and require Wordpress and Relaymark support. Unfortunately the designer that we assigned to the task let us down and did not complete the project. This is now time sensitive as we have lost weeks of working time. We require general refinement of the existing website and assistance with photos, menus etc. We also need to build a few simple customer forms. The website also needs to be FULLY mobile optimised. We have also been recommended to sign up for Relaymark (which I have done) as we will be using this for all our mailing campaigns. The designer will need to set this up for us and assist with email templates and some general assistance with helping us use Relaymark. We are looking to develop a long term partnership with a designer that can work alongside us as we grow www.quillmarsh.com.au

Coding

```html
<!DOCTYPE html>
<html lang="en">
<head>
<meta charset="utf-8">
<title>Quillmarsh – Website Refinement</title>
<link href="https://fonts.googleapis.com/css2?family=Cinzel:wght@400;500&family=Roboto:wght@400;500;700&family=Source+Sans+3:wght@400&display=swap" rel="stylesheet">
<style>
:root{
  --accent:#a96b6b;
  --ink:#111111;
  --heading:#3b3535;
  --body:#6d6d6d;
  --topbar:#e9e9e9;
  --blush:#f4ebe7;
  --white:#ffffff;
  --rule:#bdbdbd;
}
*{margin:0;padding:0;box-sizing:border-box}
html,body{width:1200px;height:1200px;overflow:hidden;background:var(--white)}
.stage{position:absolute;left:0;top:0;width:1932px;height:1932px;transform:scale(0.621118);transform-origin:0 0;}
.pitch{position:absolute;left:200px;top:582px;font-family:"Source Sans 3",sans-serif;font-size:80px;line-height:92px;color:var(--ink);letter-spacing:-0.5px}
.site{position:absolute;left:1103px;top:46px;width:517px;height:1886px;background:var(--white);font-family:Roboto,sans-serif;overflow:hidden}
.scrollbar{position:absolute;left:1620px;top:46px;width:4px;height:1886px;background:var(--rule)}
.abs{position:absolute}
.topbar{left:0;top:0;width:517px;height:19px;background:var(--topbar);display:flex;justify-content:center;gap:10px;align-items:center;font-size:6.6px;color:#666}
.nav{left:0;top:19px;width:517px;height:42px}
.brand{left:37px;top:13px;font-family:Cinzel,serif;font-size:13px;color:var(--accent);letter-spacing:.5px}
.menu{right:36px;top:15px;display:flex;gap:8px;align-items:center;font-size:6.8px;color:#444}
.menu .current{border-bottom:1px solid #444;padding-bottom:2px}
.menu .cta{background:var(--accent);color:var(--white);padding:3px 7px;border-radius:1px}
.hero{left:0;top:61px;width:515px;height:250px;background:linear-gradient(100deg,#d8c6ad 0%,#c98a6c 38%,#b35a45 55%,#a0784e 80%,#6d5a36 100%)}
.hero-title{left:275px;top:175px;font-family:Cinzel,serif;font-size:21px;color:var(--white);letter-spacing:.5px}
.hero-btn{left:326px;top:208px;width:91px;height:21px;border:1.5px solid #f1e0da;background:var(--accent);color:var(--white);font-size:6.5px;font-weight:700;display:flex;align-items:center;justify-content:center;letter-spacing:.3px}
.h-serif{font-family:Cinzel,serif;color:var(--heading);font-size:21px;line-height:23px;letter-spacing:.4px}
.copy{font-size:6.6px;line-height:10.4px;color:var(--body)}
.link{font-size:6.6px;font-weight:500;color:#444;text-decoration:underline}
.btn{background:var(--accent);color:var(--white);font-size:6.5px;font-weight:700;display:flex;align-items:center;justify-content:center;letter-spacing:.2px}
.services{left:36px;top:454px;width:445px;height:220px;border-radius:12px;overflow:hidden;display:flex}
.svc{flex:1;position:relative;display:flex;align-items:flex-end;justify-content:center;padding-bottom:30px;color:var(--white);font-size:12.5px;font-weight:500}
.svc-sell{background:linear-gradient(160deg,#b9bcb6,#9a9893 60%,#7d7570)}
.svc-buy{background:linear-gradient(160deg,#c6813c,#a9622a 60%,#7a4b2b)}
.about-band{left:0;top:721px;width:517px;height:332px;background:var(--blush)}
.about-img{left:258px;top:759px;width:259px;height:177px;border-radius:10px 0 0 10px;background:linear-gradient(120deg,#8ab2c6,#c9d6dc 45%,#e9ecec 70%,#b1b9bd)}
.feature{width:117px;height:143px;background:var(--white);border-radius:8px;box-shadow:0 2px 6px rgba(0,0,0,.08);text-align:center}
.feature svg{margin-top:14px}
.feature h3{font-size:7.6px;line-height:9px;font-weight:700;color:#222;margin-top:8px}
.feature p{font-size:6.2px;line-height:10.3px;color:var(--body);margin:6px 9px 0}
.why-img{left:0;top:1174px;width:258px;height:146px;background:linear-gradient(120deg,#cfd7d2,#eef0ee 45%,#b9c7cf 75%,#e6e6e3)}
.video{left:0;top:1375px;width:515px;height:247px;background:linear-gradient(90deg,#7b776f 0%,#c89a3a 30%,#e3b835 45%,#6b5945 65%,#8a6b4e 85%,#54483d 100%)}
.story{width:141px;height:143px;border:1px solid #ddd;border-radius:4px;overflow:hidden;background:var(--white)}
.story .pic{height:94px;background:linear-gradient(120deg,#5d7fa8,#a9c1d9 45%,#e4d3bd 60%,#496a93)}
.story h4{font-size:7.6px;font-weight:700;color:#222;margin:6px 8px 0}
.story p{font-size:6.2px;line-height:10px;color:var(--body);margin:3px 8px 0}
</style>
</head>
<body>
<div class="stage">
  <div class="pitch">Relaymark Integration<br>Mobile issue fixing<br>Custom forms</div>

  <div class="site">
    <div class="abs topbar"><span>Cost of Selling A Business</span><span>Businesses For Sale</span><span>Candidates Looking to Buy</span><span>Services</span><span>Blog</span><span>Why Choose Quillmarsh?</span></div>
    <div class="abs nav">
      <div class="abs brand">Quillmarsh</div>
      <div class="abs menu"><span class="current">Home</span><span>About us</span><span>Selling Your Business</span><span>Buy a Business</span><span>Contact</span><span>Sign In</span><span class="cta">Sell a Business</span></div>
    </div>

    <div class="abs hero" role="img" aria-label="Woman in a rust-coloured dress seated in a warm, plant-filled room"></div>
    <div class="abs hero-title">Quillmarsh</div>
    <div class="abs hero-btn">SELL A BUSINESS</div>

    <div class="abs h-serif" style="left:36px;top:349px">Our Services</div>
    <p class="abs copy" style="left:36px;top:384px;width:448px">Lorem ipsum dolor sit amet, consectetur adipiscing elit, sed do eiusod tempor incididunt ut labore et dolore magna aliqua. Quis ipsum suspe ndisse ultrices gravida. Risus commodo viverra maecenas accumsan lacus vel facilisis. Lorem ipsum dolor sit amet, consectetur adipiscing elit, sed do eiusmod tempor incididunt ut labore.</p>
    <div class="abs link" style="left:36px;top:428px">VIEW ALL SERVICES</div>

    <div class="abs services">
      <div class="svc svc-sell" role="img" aria-label="Bright hotel lobby with wicker chairs">Selling Your Business</div>
      <div class="svc svc-buy" role="img" aria-label="Warm amber lounge with rattan armchairs">Buying A Business</div>
    </div>

    <div class="abs about-band"></div>
    <div class="abs h-serif" style="left:26px;top:760px">About<br>Quillmarsh</div>
    <p class="abs copy" style="left:26px;top:821px;width:208px">Lorem ipsum dolor sit amet, consectetur adipiscing elit, sed do eiusod tempor incididunt ut labore et dolore magna aliqua. Quis ipsum suspe ndisse ultrices gravida. Risus commodo viverra maecenas accumsan lacus vel facilisis. Lorem ipsum dolor sit amet, consectetur adipiscing elit, sed do eiusmod tempor incididunt ut labore et dolore magna aliqua. Quis ipsum suspe ndisse ultrices gravida.</p>
    <div class="abs btn" style="left:26px;top:904px;width:70px;height:20px">READ MORE</div>
    <div class="abs about-img" role="img" aria-label="Two business people shaking hands over a laptop"></div>

    <div class="abs feature" style="left:74px;top:976px">
      <svg width="58" height="40" viewBox="0 0 58 40" fill="none" stroke="#a96b6b" stroke-width="1.4"><path d="M4 12l12-6 10 5 8-3 18 6-4 12-12 10-14-4L8 24z"/><path d="M22 16l8 6M26 28l6-5M18 24l5 4"/></svg>
      <h3>Expert advisors<br>at you service</h3>
      <p>Lorem ipsum dolor sit amet, contur adipiscing elit, sed do eiusmod tempor incididunt ut labore et dolore mag.</p>
    </div>
    <div class="abs feature" style="left:199px;top:976px">
      <svg width="58" height="40" viewBox="0 0 58 40" fill="none" stroke="#a96b6b" stroke-width="1.4"><circle cx="29" cy="14" r="10"/><circle cx="29" cy="12" r="3"/><path d="M24 20c1-3 9-3 10 0"/><path d="M10 26l10-4 9 4 9-4 10 4-8 10H18z"/></svg>
      <h3>A marketplace of<br>opportunity</h3>
      <p>Lorem ipsum dolor sit amet, contur adipiscing elit, sed do eiusmod tempor incididunt ut labore et dolore mag.</p>
    </div>
    <div class="abs feature" style="left:324px;top:976px">
      <svg width="58" height="40" viewBox="0 0 58 40" fill="none" stroke="#a96b6b" stroke-width="1.4"><circle cx="17" cy="5" r="3.5"/><circle cx="29" cy="5" r="3.5"/><circle cx="41" cy="5" r="3.5"/><path d="M15.5 5l1.2 1.2 2-2.4M27.5 5l1.2 1.2 2-2.4M39.5 5l1.2 1.2 2-2.4"/><circle cx="29" cy="20" r="5"/><path d="M14 30c6-3 10 0 15 0s8-3 14-1M14 30v6h22l10-7"/></svg>
      <h3>The tools you<br>need</h3>
      <p>Lorem ipsum dolor sit amet, contur adipiscing elit, sed do eiusmod tempor incididunt ut labore et dolore mag.</p>
    </div>

    <div class="abs why-img" role="img" aria-label="Smiling woman working on a laptop in a bright office"></div>
    <div class="abs h-serif" style="left:284px;top:1175px">Why Choose<br>Quillmarsh?</div>
    <p class="abs copy" style="left:284px;top:1229px;width:208px">Lorem ipsum dolor sit amet, consectetur adipiscing elit, sed do eiusod tempor incididunt ut labore et dolore magna aliqua. Quis ipsum suspe ndisse ultrices gravida. Risus commodo viverra maecenas accumsan lacus vel facilisis. Lorem ipsum dolor sit amet, consectetur adipiscing elit, sed do eiusmod tempor incididunt ut labore et dolore magna aliqua. Quis ipsum suspe ndisse ultrices gravida.</p>
    <div class="abs btn" style="left:284px;top:1311px;width:70px;height:20px">READ MORE</div>

    <div class="abs video" role="img" aria-label="Smiling café owner in an apron holding a tablet in her restaurant"></div>
    <svg class="abs" style="left:240px;top:1484px" width="36" height="36" viewBox="0 0 36 36"><circle cx="18" cy="18" r="16.5" fill="rgba(0,0,0,.15)" stroke="#fff" stroke-width="1.6"/><path d="M14 11l11 7-11 7z" fill="#fff"/></svg>

    <div class="abs h-serif" style="left:0;top:1661px;width:517px;text-align:center">Get Inspired.<br>Read Recent Success Stories</div>

    <div class="abs story" style="left:36px;top:1716px"><div class="pic" role="img" aria-label="Businesswoman with a tablet outside a glass office building"></div><h4>Lorem ipsum dolor sit amet</h4><p>Lorem ipsum dolor sit amet, conse ctetur adipiscing elit, sed do.</p></div>
    <div class="abs story" style="left:187px;top:1716px"><div class="pic" role="img" aria-label="Businesswoman with a tablet outside a glass office building"></div><h4>Lorem ipsum dolor sit amet</h4><p>Lorem ipsum dolor sit amet, conse ctetur adipiscing elit, sed do.</p></div>
    <div class="abs story" style="left:338px;top:1716px"><div class="pic" role="img" aria-label="Businesswoman with a tablet outside a glass office building"></div><h4>Lorem ipsum dolor sit amet</h4><p>Lorem ipsum dolor sit amet, conse ctetur adipiscing elit, sed do.</p></div>
  </div>
  <div class="scrollbar"></div>
</div>
</body>
</html>
```